Website Needs Designing / Populating

We are a Business Consultancy in London. We are Headhunters and Recruitment. I have bought the Domain, and Wordpress Site, installed a template from Pagecraft Yard. I have tried to do it myself but do not have the time to complete or do it as I want / need.
I have some 'stock' pics and a logo - see uploaded logo files.
I want an easy to use Website - tells clients and viewers what we are about.
We are a recruitment / Headhunting Consultancy so some visitors may want to apply for positions through loading their CV / Details through the site.
We want to be about friendly but expertise. Honest and trustworthy with a heavy emphasis on Consultancy!

Target Market(s)

IT and Finance Job Seekers. Our clients are in the Marketing Communications sectors so needs to be appealing to that market

Industry/Entity Type

Business Consultant

Number of Pages Required

3 page

Requirements
Must have
• Our Logo as a central theme - see uploaded files
Nice to have
• Simple. Easy to use, inviting

```html
<!DOCTYPE html>
<html lang="en">
<head>
<meta charset="utf-8">
<title>Ledgerline Recruitment</title>
<link href="https://fonts.googleapis.com/css2?family=Lato:wght@300;400;700&display=swap" rel="stylesheet">
<style>
:root{
  --blue:#1a8fd8;
  --blue-dark:#0f78bd;
  --teal:#3bb3a4;
  --purple:#6b2d8f;
  --yellow:#f7c600;
  --ink:#2b2f33;
  --muted:#8a8f94;
  --line:#e1e4e6;
  --panel:#f3f3f3;
  --footer:#232d31;
  --footer-base:#1a2124;
  --footer-text:#b9c0c4;
}
*{box-sizing:border-box;margin:0;padding:0}
html,body{width:692px;height:1200px;overflow:hidden}
body{font-family:"Lato",sans-serif;color:var(--ink);background:#fff;position:relative}
a{color:inherit;text-decoration:none}

.site-header{position:absolute;left:0;top:0;width:692px;height:76px;border-top:2px solid var(--blue);background:#fff}
.brand{position:absolute;left:76px;top:14px}
.brand-name{font-size:25px;font-weight:400;color:#4a4f55;letter-spacing:-.5px;line-height:28px}
.brand-sub{font-size:9px;font-weight:400;color:#4a4f55;letter-spacing:8.6px;margin-top:2px}
.top-contact{position:absolute;right:76px;top:17px;font-size:7px;color:#333;display:flex;gap:12px;align-items:center}
.top-contact span{display:flex;align-items:center;gap:5px}
.main-nav{position:absolute;top:47px;left:0;font-size:6.6px;color:#555;text-transform:uppercase}
.main-nav a{position:absolute;white-space:nowrap}
.main-nav .active{color:var(--blue)}

.hero{position:absolute;left:0;top:76px;width:692px;height:271px;background:linear-gradient(120deg,#2c3a48 0%,#5b6168 40%,#8a7a66 60%,#3a3f45 100%)}
.hero-caption{position:absolute;left:76px;top:32px;width:194px;height:150px;background:rgba(26,143,216,.88);padding:16px 14px;color:#fff}
.hero-caption h1{font-size:17px;font-weight:400;line-height:20px;letter-spacing:0;white-space:nowrap}
.hero-caption p{font-size:6.5px;font-weight:400;line-height:13px;margin-top:8px}
.btn-dark{display:inline-block;margin-top:10px;background:#222;color:#fff;font-size:6.5px;padding:7px 12px;border-radius:2px}
.hero-dots{position:absolute;left:76px;top:196px;display:flex;gap:5px}
.hero-dots i{width:3px;height:3px;border-radius:50%;background:#fff}
.hero-dots i:first-child{background:var(--blue)}

.services{position:absolute;left:76px;top:297px;width:540px;height:253px;background:#fff;box-shadow:0 6px 10px rgba(0,0,0,.06)}
.section-title{font-size:17px;font-weight:400;text-align:center;letter-spacing:.3px;color:var(--ink)}
.service{position:absolute;top:50px;width:180px;text-align:center}
.service-icon{width:66px;height:66px;border-radius:50%;margin:0 auto;display:flex;align-items:center;justify-content:center}
.service-shadow{width:50px;height:5px;margin:4px auto 0;border-radius:50%;background:rgba(0,0,0,.08)}
.service h3{font-size:11px;font-weight:400;margin-top:16px}
.service p{font-size:6.3px;font-weight:300;color:var(--muted);line-height:12.8px;margin-top:7px}
.btn-blue{display:inline-block;margin-top:12px;background:var(--blue);color:#fff;font-size:6.5px;padding:6px 7px;border-radius:2px;border-bottom:2px solid var(--blue-dark)}

.recommends{position:absolute;left:0;top:550px;width:692px;height:272px;background:var(--panel)}
.rec{position:absolute;top:80px;width:130px}
.rec-photo{width:122px;height:64px;border:2px solid #fff;box-shadow:0 1px 3px rgba(0,0,0,.15)}
.rec h3{font-size:11px;font-weight:400;margin-top:29px}
.rec p{font-size:6.3px;font-weight:300;color:var(--muted);line-height:12.8px;margin-top:5px}

.news{position:absolute;left:0;top:822px;width:692px;height:190px;background:#fff}
.news h2{position:absolute;left:76px;top:29px;font-size:17px;font-weight:400}
.news-arrows{position:absolute;left:580px;top:30px;display:flex;gap:13px}
.news-card{position:absolute;top:69px;width:170px;height:91px;border:1px solid var(--line);padding:10px 11px}
.news-card h3{font-size:8px;font-weight:400;line-height:12px;text-transform:uppercase}
.news-card time{display:block;font-size:6px;font-weight:300;color:var(--muted);margin-top:5px}
.news-card p{font-size:6.3px;font-weight:300;color:var(--muted);line-height:12.8px;margin-top:3px}

.site-footer{position:absolute;left:0;top:1012px;width:692px;height:142px;background:var(--footer);color:var(--footer-text)}
.footer-col{position:absolute;top:22px}
.footer-col h4{font-size:8px;font-weight:400;color:#fff;margin-bottom:9px}
.footer-col li{list-style:none;font-size:6.3px;font-weight:300;line-height:12px}
.contact-line{display:flex;gap:6px;font-size:6.3px;font-weight:300;line-height:12px}
.footer-brand{position:absolute;left:478px;top:18px}
.footer-brand .brand-name,.footer-brand .brand-sub{color:#c9ced1}
.social{position:absolute;left:521px;top:66px;display:flex;gap:5px}
.social i{width:20px;height:20px;border-radius:50%}
.copyright{position:absolute;left:0;top:1154px;width:692px;height:46px;background:var(--footer-base);color:#9aa3a7;font-size:6.3px;font-weight:300;text-align:center;line-height:46px}
</style>
</head>
<body>

<header class="site-header">
  <div class="brand">
    <div class="brand-name">Ledgerline</div>
    <div class="brand-sub">Recruitment</div>
  </div>
  <div class="top-contact">
    <span><svg width="7" height="7" viewBox="0 0 10 10"><path d="M2 1l2 2-1 1.5c.8 1.5 1.8 2.5 3.5 3.5L8 7l2 2-1.5 1C4.5 10 0 5.5 1 1.5z" fill="#333"/></svg>0800-555-014</span>
    <span><svg width="8" height="6" viewBox="0 0 10 7"><rect x=".5" y=".5" width="9" height="6" fill="none" stroke="#333"/><path d="M.5.5l4.5 3.5L9.5.5" fill="none" stroke="#333"/></svg>HELLO@LEDGERLINE.EXAMPLE</span>
  </div>
  <nav class="main-nav">
    <a class="active" style="left:270px">Home</a>
    <a style="left:311px">Training</a>
    <a style="left:365px">Consulting</a>
    <a style="left:430px">Personnel Leasing</a>
    <a style="left:519px">About Us</a>
    <a style="left:574px">Contact Us</a>
  </nav>
</header>

<section class="hero" role="img" aria-label="Team of smiling business colleagues gathered around a document in a bright office">
  <div class="hero-caption">
    <h1>HEADHUNTERS AND<br>RECRUITMENT</h1>
    <p>Neque porro quisquam est, qui dolorem ipsum quia dolor sit amet, consectetur</p>
    <a class="btn-dark">Read More</a>
  </div>
  <div class="hero-dots"><i></i><i></i><i></i></div>
</section>

<section class="services">
  <h2 class="section-title" style="margin-top:20px">OUR SERVICES</h2>
  <div class="service" style="left:7px">
    <div class="service-icon" style="background:var(--teal)">
      <svg width="26" height="26" viewBox="0 0 26 26" fill="none" stroke="#fff" stroke-width="1.3"><circle cx="13" cy="9" r="5"/><path d="M3 23c0-5 4.5-8 10-8s10 3 10 8z"/></svg>
    </div>
    <div class="service-shadow"></div>
    <h3>CONSULTANCY</h3>
    <p>Neque porro quisquam est qui dolorem ipsum<br>quia dolor sadipisci velit...</p>
    <a class="btn-blue">Read More</a>
  </div>
  <div class="service" style="left:180px">
    <div class="service-icon" style="background:var(--purple)">
      <svg width="26" height="26" viewBox="0 0 26 26" fill="none" stroke="#fff" stroke-width="1.3"><rect x="2" y="4" width="22" height="14"/><path d="M13 18v4M9 24l4-2 4 2M6 13l2-4 2 4 2-4M16 11a2 2 0 1 0 4 0a2 2 0 1 0-4 0"/></svg>
    </div>
    <div class="service-shadow"></div>
    <h3>HEADHUNTERS</h3>
    <p>Neque porro quisquam est qui dolorem ipsum<br>quia dolor sadipisci velit...</p>
    <a class="btn-blue">Read More</a>
  </div>
  <div class="service" style="left:350px">
    <div class="service-icon" style="background:var(--yellow)">
      <svg width="26" height="26" viewBox="0 0 26 26" fill="none" stroke="#fff" stroke-width="1.3"><circle cx="13" cy="11" r="7"/><path d="M6 11a7 7 0 0 0 14 0M13 18v4M9 23h8"/></svg>
    </div>
    <div class="service-shadow"></div>
    <h3>RECRUITMENT</h3>
    <p>Neque porro quisquam est qui dolorem ipsum<br>quia dolor sadipisci velit...</p>
    <a class="btn-blue">Read More</a>
  </div>
</section>

<section class="recommends">
  <h2 class="section-title" style="padding-top:32px">LEDGERLINE RECOMMENDS</h2>
  <article class="rec" style="left:76px">
    <div class="rec-photo" role="img" aria-label="Hand holding a tablet showing a grid of candidate profiles" style="background:linear-gradient(135deg,#5b6f80,#9fb3c0)"></div>
    <h3>HEADHUNTING</h3>
    <p>Lorem ipsum dolor sit amet, consectetur adipiscing elit, sed do eiusmod tempor incididunt ut labore</p>
  </article>
  <article class="rec" style="left:215px">
    <div class="rec-photo" role="img" aria-label="Stressed woman at a laptop in a white room" style="background:linear-gradient(135deg,#f0e6ea,#c9b4bd)"></div>
    <h3>MEDIATION</h3>
    <p>Lorem ipsum dolor sit amet, consectetur adipiscing elit, sed do eiusmod tempor incididunt ut labore</p>
  </article>
  <article class="rec" style="left:352px">
    <div class="rec-photo" role="img" aria-label="Group of office colleagues seen from above" style="background:linear-gradient(135deg,#dfe4e8,#6f7c86)"></div>
    <h3>GAMIFICATION</h3>
    <p>Lorem ipsum dolor sit amet, consectetur adipiscing elit, sed do eiusmod tempor incididunt ut labore</p>
  </article>
  <article class="rec" style="left:490px">
    <div class="rec-photo" role="img" aria-label="Cheerful business team giving thumbs up" style="background:linear-gradient(135deg,#e8ecef,#8a8f96)"></div>
    <h3>MOTIVATION</h3>
    <p>Lorem ipsum dolor sit amet, consectetur adipiscing elit, sed do eiusmod tempor incididunt ut labore</p>
  </article>
</section>

<section class="news">
  <h2>RECENT NEWS</h2>
  <div class="news-arrows">
    <svg width="10" height="16" viewBox="0 0 10 16"><path d="M9 1L2 8l7 7" fill="none" stroke="#333" stroke-width="1.2"/></svg>
    <svg width="10" height="16" viewBox="0 0 10 16"><path d="M1 1l7 7-7 7" fill="none" stroke="#333" stroke-width="1.2"/></svg>
  </div>
  <article class="news-card" style="left:76px">
    <h3>Starting a new business? Don`t dive in!</h3>
    <time>FEB 25,2016</time>
    <p>Neque porro quisquam est qui dolorem ipsum quia dolor, adipisci velit...</p>
  </article>
  <article class="news-card" style="left:261px">
    <h3>Effective, trusted &amp; affordable business consultant</h3>
    <time>FEB 25,2016</time>
    <p>Neque porro quisquam est qui dolorem ipsum quia dolor, adipisci velit...</p>
  </article>
  <article class="news-card" style="left:446px">
    <h3>To ensure you achieve your goals</h3>
    <time>FEB 25,2016</time>
    <p>Neque porro quisquam est qui dolorem ipsum quia dolor, adipisci velit...</p>
  </article>
</section>

<footer class="site-footer">
  <div class="footer-col" style="left:77px">
    <h4>QUICK LINKS</h4>
    <ul><li>Home</li><li>Training</li><li>Consulting</li><li>Jobs</li><li>Personnel Leasing</li><li>CV Consultation</li><li>About us</li></ul>
  </div>
  <div class="footer-col" style="left:192px">
    <h4>COMPANY</h4>
    <ul><li>Job seekers</li><li>Employers</li><li>Login</li><li>Sign Up</li></ul>
  </div>
  <div class="footer-col" style="left:289px">
    <h4>CONTACT US</h4>
    <div class="contact-line"><svg width="6" height="8" viewBox="0 0 6 8"><path d="M3 0a3 3 0 0 0-3 3c0 2 3 5 3 5s3-3 3-5a3 3 0 0 0-3-3z" fill="#b9c0c4"/></svg><span>Neque porro quisquam est qui dolorem ipsum<br>quia dolor sit adipisci velit...</span></div>
    <div class="contact-line" style="margin-top:12px"><svg width="6" height="8" viewBox="0 0 6 8"><rect x=".5" y=".5" width="5" height="7" rx="1" fill="none" stroke="#b9c0c4"/></svg><span>0800-555-014-200</span></div>
    <div class="contact-line"><svg width="7" height="7" viewBox="0 0 7 7"><rect x=".5" y="2" width="6" height="4.5" fill="#b9c0c4"/><rect x="1.5" y=".5" width="4" height="2" fill="none" stroke="#b9c0c4"/></svg><span>0800-555-014-200</span></div>
    <div class="contact-line"><svg width="7" height="6" viewBox="0 0 7 6"><rect x=".5" y=".5" width="6" height="5" fill="none" stroke="#b9c0c4"/><path d="M.5.5l3 2.5 3-2.5" fill="none" stroke="#b9c0c4"/></svg><span>hello@ledgerline.example</span></div>
  </div>
  <div class="footer-brand">
    <div class="brand-name">Ledgerline</div>
    <div class="brand-sub">Recruitment</div>
  </div>
  <div class="social">
    <i style="background:#3b5a9a"></i><i style="background:#2ea3e6"></i><i style="background:#f39c1a"></i><i style="background:#d6202b"></i>
  </div>
</footer>
<div class="copyright">Copyright © 2016 Ledgerline. All right Reserved.</div>

</body>
</html>
```